Need DL Flyer for Real Estate Drops

We need a real estate flyer ,double sided. With content on 1 side like: Want to know what's your house is worth " contact us today and on other side agent details. We are looking for an ongoing partnership with designer so this assignment will be ongoing

```html
<!DOCTYPE html>
<html lang="en">
<head>
<meta charset="utf-8">
<title>Kestrel Real Estate – DL Flyer</title>
<link href="https://fonts.googleapis.com/css2?family=Inter:wght@400;500;600;800&family=Oswald:wght@600;700&family=Great+Vibes&display=swap" rel="stylesheet">
<style>
  :root {
    --navy: #0c1633;
    --red: #cf2229;
    --sky: #a9c7ec;
    --white: #ffffff;
    --backdrop: #bcbcbc;
  }
  * { margin: 0; padding: 0; box-sizing: border-box; }
  html, body { width: 1193px; height: 1200px; overflow: hidden; }
  body { background: var(--backdrop); position: relative; font-family: "Inter", sans-serif; }

  .flyer { position: absolute; top: 228px; width: 354px; height: 744px; overflow: hidden; background: var(--white); }
  .flyer--front { left: 215px; }
  .flyer--back { left: 622px; }

  .brand { position: absolute; left: 54px; top: 32px; display: flex; align-items: center; gap: 18px; }
  .brand__mark { width: 70px; height: 70px; background: var(--red); }
  .brand__name { color: var(--navy); font-weight: 600; line-height: 1; text-align: center; }
  .brand__word { display: block; font-size: 42px; letter-spacing: -0.5px; }
  .brand__sub { display: block; font-size: 12px; letter-spacing: 3.4px; margin-top: 4px; }

  .front__sky { position: absolute; left: 0; top: 0; width: 100%; height: 120px; background: var(--sky); }
  .front__photo {
    position: absolute; left: 0; top: 120px; width: 100%; height: 376px;
    background: linear-gradient(180deg, #a9c7ec 0%, #cfdde8 20%, #f1f3f2 42%, #8fa27a 60%, #3f8fb0 72%, #7fb6cc 84%, #e8ecee 100%);
  }
  .front__copy { position: absolute; left: 0; top: 490px; width: 100%; text-align: center; }
  .front__script { font-family: "Great Vibes", cursive; color: var(--red); font-size: 44px; line-height: 1; }
  .front__headline { font-family: "Oswald", sans-serif; font-weight: 700; color: var(--navy); text-transform: uppercase; line-height: 1; }
  .front__headline--big { font-size: 57px; margin-top: 0; letter-spacing: -0.5px; }
  .front__headline--mid { font-size: 45px; margin-top: 2px; letter-spacing: -0.5px; }
  .front__cta { color: var(--red); font-size: 20px; margin-top: 14px; letter-spacing: 0.3px; }
  .front__phone {
    margin: 4px auto 0; width: 268px; height: 34px; border-radius: 17px;
    background: linear-gradient(180deg, #3a4a6c 0%, var(--navy) 55%, #050a1c 100%);
    display: flex; align-items: center; justify-content: center; gap: 6px;
    color: var(--white); font-weight: 800; font-size: 30px; letter-spacing: 0.5px;
  }
  .front__phone svg { width: 20px; height: 20px; }
  .front__web { color: var(--red); font-size: 17px; margin-top: 2px; letter-spacing: 0.3px; }
  .front__web b { font-weight: 800; }

  .back__portrait {
    position: absolute; left: 62px; top: 115px; width: 211px; height: 247px;
    background: linear-gradient(180deg, #f4f4f4 0%, #bdbdbd 45%, #8e8e8e 100%);
  }
  .back__panel { position: absolute; left: 0; top: 362px; width: 100%; height: 382px; background: var(--navy); text-align: center; color: var(--white); }
  .back__stripe { position: absolute; left: 0; top: 5px; width: 100%; height: 7px; background: var(--red); }
  .agent__name { font-family: "Oswald", sans-serif; font-weight: 700; font-size: 30px; margin-top: 38px; line-height: 1.1; letter-spacing: -0.3px; }
  .agent__role { color: var(--red); font-size: 17.5px; line-height: 22px; }
  .agent__rule { width: 58px; height: 1px; background: var(--white); margin: 12px auto 9px; }
  .agent__address { font-size: 15.5px; line-height: 20px; }
  .contact-icons { display: flex; justify-content: center; gap: 5px; margin-top: 12px; }
  .contact-icons span { width: 28px; height: 28px; border-radius: 50%; background: var(--red); display: flex; align-items: center; justify-content: center; }
  .contact-icons svg { width: 14px; height: 14px; }
  .agent__phone { font-size: 22px; line-height: 28px; margin-top: 8px; letter-spacing: 0.5px; }
  .agent__line { font-size: 15.5px; line-height: 19px; }
  .social { display: flex; justify-content: center; gap: 4px; margin-top: 13px; }
  .social span { width: 25px; height: 25px; border-radius: 50%; background: var(--red); }
</style>
</head>
<body>

<section class="flyer flyer--front">
  <div class="front__sky"></div>
  <div class="brand">
    <div class="brand__mark"></div>
    <div class="brand__name"><span class="brand__word">kestrel</span><span class="brand__sub">REAL ESTATE</span></div>
  </div>
  <div class="front__photo" role="img" aria-label="Photo of a modern white two-storey house with a swimming pool and garden under a blue sky"></div>
  <div class="front__copy">
    <p class="front__script">Want to know</p>
    <p class="front__headline front__headline--big">What's your</p>
    <p class="front__headline front__headline--mid">House is worth?</p>
    <p class="front__cta">CONTACT US TODAY</p>
    <div class="front__phone">
      <svg viewBox="0 0 24 24" fill="none" stroke="#fff" stroke-width="1.6"><path d="M5 3h4l2 5-2.5 1.5a11 11 0 0 0 6 6L16 13l5 2v4a2 2 0 0 1-2 2A16 16 0 0 1 3 5a2 2 0 0 1 2-2z"/></svg>
      <span>03 9012 3456</span>
    </div>
    <p class="front__web">www.<b>kestrelrealestate</b>.com.au</p>
  </div>
</section>

<section class="flyer flyer--back">
  <div class="brand">
    <div class="brand__mark"></div>
    <div class="brand__name"><span class="brand__word">kestrel</span><span class="brand__sub">REAL ESTATE</span></div>
  </div>
  <div class="back__portrait" role="img" aria-label="Black and white portrait photo of the agent in a suit"></div>
  <div class="back__panel">
    <div class="back__stripe"></div>
    <h1 class="agent__name">ROHAN MEHTA</h1>
    <p class="agent__role">Managing Director/LEA</p>
    <p class="agent__role">Kestrel Real Estate</p>
    <div class="agent__rule"></div>
    <p class="agent__address">14/8 Harbour Lane<br>Westfield 3100</p>
    <div class="contact-icons">
      <span><svg viewBox="0 0 24 24" fill="#fff"><path d="M5 3h4l2 5-2.5 1.5a11 11 0 0 0 6 6L16 13l5 2v4a2 2 0 0 1-2 2A16 16 0 0 1 3 5a2 2 0 0 1 2-2z"/></svg></span>
      <span><svg viewBox="0 0 24 24" fill="none" stroke="#fff" stroke-width="2.4"><rect x="7" y="2" width="10" height="20" rx="2"/><line x1="11" y1="18" x2="13" y2="18"/></svg></span>
      <span><svg viewBox="0 0 24 24" fill="#fff"><path d="M2 5h20v14H2z"/><path d="M2 5l10 8 10-8" fill="none" stroke="#cf2229" stroke-width="2"/></svg></span>
      <span><svg viewBox="0 0 24 24" fill="none" stroke="#fff" stroke-width="2"><circle cx="12" cy="12" r="9"/><ellipse cx="12" cy="12" rx="4" ry="9"/><line x1="3" y1="12" x2="21" y2="12"/></svg></span>
    </div>
    <p class="agent__phone">03 9012 3456</p>
    <p class="agent__phone" style="margin-top:0">0400111222</p>
    <p class="agent__line">rohan@kestrelrealestate.com.au</p>
    <p class="agent__line">kestrelrealestate.com.au</p>
    <div class="social"><span></span><span></span></div>
  </div>
</section>

</body>
</html>
```